Recreate a label for a champagne bottle [See attached example]

I'm needing to recreate a label for a champagne bottle label to give as closing gifts to clients when they purchase a home. Please include the following text "Welcome Home", my initials "R.T", "Established Year", the hashtag #BubTORVA and my logo (attached). I prefer to have a black or white background with a crisp, easy to read cursive font similar to the Dunmore bourbon font. I want it to look as similar of a layout to the Valdorca label as possible

Target Market(s)

Luxury

Font styles to use
Decorative
Script

Colors

Designer to choose only greyscale colors for use in the design.

Requirements
Must have
• "Welcome Home", my initials "R.T", "Established Year", the hashtag #BubTORVA and my logo
Nice to have
• Clean cursive font, easy to read, luxury look.
Should not have
• Clutter, too much design.

```html
<!DOCTYPE html>
<html lang="en">
<head>
<meta charset="utf-8">
<title>Welcome Home – Champagne Label Set</title>
<link rel="stylesheet" href="https://fonts.googleapis.com/css2?family=Cinzel:wght@700&family=Pinyon+Script&family=Lato:wght@400&display=swap">
<style>
  :root{
    --paper:#ffffff;
    --ink:#0b0b0b;
    --label-black:#141414;
    --silver-white:#ffffff;
    --silver-grey:#c9c9c9;
    --metal-light:#f2f2f2;
    --metal-mid:#bdbdbd;
    --metal-deep:#7a7a7a;
    --collar-dark:#161616;
    --collar-light:#444444;
    --accent-light:#e6e6e6;
  }
  *{margin:0;padding:0;box-sizing:border-box}
  html,body{width:1200px;height:849px;overflow:hidden;background:var(--paper)}
  .canvas{position:relative;width:1200px;height:849px}
  .neck-foil{position:absolute;left:500px;top:168px;width:274px;height:537px}
  .body-label{position:absolute;left:796px;width:343px;height:296px}
  .label-white{top:123px}
  .label-black{top:444px}
  .t-brand{font-family:"Cinzel",serif;font-weight:700;letter-spacing:5px}
  .t-year{font-family:"Cinzel",serif;font-weight:700}
  .t-script{font-family:"Pinyon Script",cursive}
  .t-initials{font-family:"Lato",sans-serif;font-weight:400;letter-spacing:-1px}
  .t-hashtag{font-family:"Lato",sans-serif;font-weight:400}
</style>
</head>
<body>
<main class="canvas">

  <svg class="neck-foil" viewBox="0 0 274 537" aria-label="Neck foil with Welcome Home and 2023 collar">
    <defs>
      <linearGradient id="foil" x1="0" x2="1">
        <stop offset="0" stop-color="var(--metal-deep)"/>
        <stop offset=".25" stop-color="var(--metal-light)"/>
        <stop offset=".5" stop-color="var(--metal-mid)"/>
        <stop offset=".75" stop-color="var(--metal-light)"/>
        <stop offset="1" stop-color="var(--metal-deep)"/>
      </linearGradient>
      <linearGradient id="collar" x1="0" x2="1">
        <stop offset="0" stop-color="var(--collar-dark)"/>
        <stop offset="1" stop-color="var(--collar-light)"/>
      </linearGradient>
      <linearGradient id="medal" x1="0" x2="1" y1="0" y2="1">
        <stop offset="0" stop-color="var(--metal-light)"/>
        <stop offset="1" stop-color="var(--metal-deep)"/>
      </linearGradient>
    </defs>
    <path fill="url(#foil)" d="M58 18 Q58 2 80 2 L195 2 Q217 2 217 18 L217 42 Q206 52 205 70 L206 200 Q214 300 244 400 L30 400 Q60 300 68 200 L69 70 Q68 52 58 42 Z"/>
    <rect x="64" y="34" width="146" height="4" fill="var(--metal-deep)" opacity=".5"/>
    <text class="t-script" font-size="56" text-anchor="middle" fill="var(--ink)" transform="translate(150 212) rotate(-90)">Welcome Home</text>
    <path fill="url(#collar)" d="M27 390 L95 383 Q108 364 136 362 Q164 364 177 383 L247 390 L274 492 L212 489 Q192 530 136 535 Q80 530 60 489 L0 492 Z"/>
    <path fill="none" stroke="var(--accent-light)" stroke-width="1.8" d="M28 398 L98 391 Q111 371 136 370 Q161 371 174 391 L246 398"/>
    <path fill="none" stroke="var(--accent-light)" stroke-width="1.8" d="M4 484 L64 481 Q84 522 136 526 Q188 522 208 481 L270 484"/>
    <circle cx="136" cy="422" r="41" fill="url(#medal)"/>
    <text class="t-year" x="136" y="432" font-size="28" text-anchor="middle" fill="var(--ink)">2023</text>
  </svg>

  <svg class="body-label label-white" viewBox="0 0 350 302" aria-label="White body label">
    <defs>
      <linearGradient id="silver" x1="0" x2="1">
        <stop offset="0" stop-color="var(--silver-white)"/>
        <stop offset=".6" stop-color="var(--silver-white)"/>
        <stop offset="1" stop-color="var(--silver-grey)"/>
      </linearGradient>
    </defs>
    <path fill="url(#silver)" d="M0 22 L118 28 Q128 28 134 16 Q148 0 175 0 Q202 0 216 16 Q222 28 232 28 L350 22 L350 288 Q175 300 0 288 Z"/>
    <path fill="none" stroke="var(--ink)" stroke-width="4" d="M8 30 L122 35 Q132 35 138 23 Q150 8 175 8 Q200 8 212 23 Q218 35 228 35 L342 30 L342 280 Q175 292 8 280 Z"/>
    <path fill="none" stroke="var(--ink)" stroke-width="1.2" d="M15 40 L335 38 L335 272 Q175 284 15 272 Z"/>
    <text class="t-brand" x="175" y="84" font-size="32" text-anchor="middle" fill="var(--ink)">TORVA</text>
    <text class="t-year" x="175" y="140" font-size="36" text-anchor="middle" fill="var(--ink)">2023</text>
    <text class="t-script" x="175" y="188" font-size="46" text-anchor="middle" fill="var(--ink)">Welcome Home</text>
    <path fill="none" stroke="var(--ink)" stroke-width="1.5" d="M60 218 Q80 212 100 215 Q120 218 140 215 M210 215 Q230 212 250 215 Q270 219 290 213"/>
    <text class="t-initials" x="175" y="230" font-size="34" text-anchor="middle" fill="var(--ink)">R.T</text>
    <text class="t-hashtag" x="175" y="264" font-size="21" text-anchor="middle" fill="var(--ink)">#BubTORVA</text>
  </svg>

  <svg class="body-label label-black" viewBox="0 0 350 302" aria-label="Black body label">
    <defs>
      <linearGradient id="metal-line" x1="0" x2="1">
        <stop offset="0" stop-color="var(--metal-deep)"/>
        <stop offset=".5" stop-color="var(--metal-light)"/>
        <stop offset="1" stop-color="var(--metal-deep)"/>
      </linearGradient>
    </defs>
    <path fill="var(--label-black)" d="M0 22 L118 28 Q128 28 134 16 Q148 0 175 0 Q202 0 216 16 Q222 28 232 28 L350 22 L350 288 Q175 300 0 288 Z"/>
    <path fill="none" stroke="url(#metal-line)" stroke-width="4" d="M8 30 L122 35 Q132 35 138 23 Q150 8 175 8 Q200 8 212 23 Q218 35 228 35 L342 30 L342 280 Q175 292 8 280 Z"/>
    <path fill="none" stroke="url(#metal-line)" stroke-width="1.2" d="M15 40 L335 38 L335 272 Q175 284 15 272 Z"/>
    <text class="t-brand" x="175" y="84" font-size="32" text-anchor="middle" fill="var(--accent-light)">TORVA</text>
    <text class="t-year" x="175" y="140" font-size="36" text-anchor="middle" fill="var(--accent-light)">2023</text>
    <text class="t-script" x="175" y="188" font-size="46" text-anchor="middle" fill="var(--accent-light)">Welcome Home</text>
    <path fill="none" stroke="var(--accent-light)" stroke-width="1.5" d="M60 218 Q80 212 100 215 Q120 218 140 215 M210 215 Q230 212 250 215 Q270 219 290 213"/>
    <text class="t-initials" x="175" y="230" font-size="34" text-anchor="middle" fill="var(--accent-light)">R.T</text>
    <text class="t-hashtag" x="175" y="264" font-size="21" text-anchor="middle" fill="var(--accent-light)">#BubTORVA</text>
  </svg>

</main>
</body>
</html>
```